Business Card Design Project

We need a Business Card Design for our Architectural Company, we want the cards to stand out WOW factor, we are thinking to have the logo on the front and embossed and all the contact info etc on the back. however we are open to suggestions

Target Market(s)

Adults looking for a Architect for their design project, or a developers who need an architecture firm to partner with. Card should be very powerful and portray elegance and creativity as first impression

Industry/Entity Type

Business

Requirements
Must have
• Must have large logo and easy to read address info, current card attached for address and contact info that should be on card.

```html
<!DOCTYPE html>
<html lang="en">
<head>
<meta charset="utf-8">
<title>Coral Bay Design Studio — Business Cards</title>
<link rel="stylesheet" href="https://fonts.googleapis.com/css2?family=Open+Sans:wght@400;600;700;800&display=swap">
<style>
  :root {
    --navy: #262d7e;
    --royal: #3f46a6;
    --royal-light: #5a62c0;
    --name-blue: #5a63b6;
    --accent-red: #e0232e;
    --ink: #1d1d1f;
    --muted: #6b6b70;
    --paper: #ffffff;
    --backdrop: #ecebe8;
  }
  * { margin: 0; padding: 0; box-sizing: border-box; }
  html, body {
    width: 1200px; height: 800px; overflow: hidden;
    background: var(--backdrop);
    font-family: "Open Sans", sans-serif;
  }
  .stage { position: relative; width: 1200px; height: 800px; }

  /* Back of card (portrait) */
  .card-back {
    position: absolute; left: 90px; top: 130px;
    width: 320px; height: 540px;
    background: linear-gradient(160deg, var(--royal) 0%, var(--royal-light) 55%, var(--royal) 100%);
    box-shadow: 0 12px 30px rgba(0,0,0,.25);
  }
  .card-back__name {
    position: absolute; left: 50%; top: 50%;
    transform: translate(-50%, -50%) rotate(90deg);
    width: 460px; text-align: center;
    color: var(--paper); font-weight: 800;
    font-size: 34px; line-height: 1.05; letter-spacing: .5px;
    text-transform: uppercase;
  }

  /* Front of card (landscape) */
  .card-front {
    position: absolute; left: 460px; top: 200px;
    width: 660px; height: 390px;
    background: var(--paper);
    box-shadow: 0 12px 30px rgba(0,0,0,.25);
    overflow: hidden;
  }
  .brand {
    position: absolute; left: 40px; top: 36px;
    display: flex; align-items: center; gap: 14px;
  }
  .brand__square { width: 30px; height: 30px; background: var(--navy); }
  .brand__name {
    color: var(--navy); font-weight: 800; font-size: 30px;
    line-height: 1.05; text-transform: uppercase;
  }
  .person { position: absolute; left: 40px; top: 150px; }
  .person__name {
    color: var(--name-blue); font-weight: 700; font-size: 22px;
    letter-spacing: .5px; text-transform: uppercase;
  }
  .person__title { color: var(--muted); font-size: 14px; margin-top: 2px; }

  .contact {
    position: absolute; left: 300px; top: 220px;
    color: var(--ink); font-size: 15px; line-height: 1.45;
  }
  .contact__address { margin-bottom: 10px; }
  .contact__row { display: flex; align-items: center; gap: 10px; }
  .contact__icon { width: 16px; height: 16px; flex: none; }

  .edge-band {
    position: absolute; right: 0; top: 0;
    width: 46px; height: 100%;
    background: var(--navy);
    border-left: 4px solid var(--paper);
    box-shadow: -3px 0 0 var(--accent-red);
  }
  .edge-band__web {
    position: absolute; left: 50%; top: 50%;
    transform: translate(-50%, -50%) rotate(90deg);
    color: var(--paper); font-size: 14px; letter-spacing: 6px;
    white-space: nowrap;
  }
</style>
</head>
<body>
<main class="stage">
  <section class="card-back" aria-label="Card back">
    <p class="card-back__name">Coral Bay<br>Design Studio<br>Ltd</p>
  </section>

  <section class="card-front" aria-label="Card front">
    <div class="brand">
      <span class="brand__square"></span>
      <span class="brand__name">Coral Bay<br>Design Studio Ltd</span>
    </div>

    <div class="person">
      <p class="person__name">Marcus Whitfield</p>
      <p class="person__title">Managing Director</p>
    </div>

    <div class="contact">
      <p class="contact__address">Harbour Point, Suite 7<br>P.O. Box 40517, Grand Cayman<br>KY1-2040, Cayman Islands</p>
      <p class="contact__row">
        <svg class="contact__icon" viewBox="0 0 16 16"><rect width="16" height="16" rx="2" fill="#3f46a6"/><path d="M5 4c-1 1-1 3 1 5s4 2 5 1l-1.5-1.5-1 .6C7.5 8.6 7.4 8.5 6.9 7.6l.6-1L6 5z" fill="#fff"/></svg>
        (345) 555-0142
      </p>
      <p class="contact__row">
        <svg class="contact__icon" viewBox="0 0 16 16"><rect width="16" height="16" rx="2" fill="#3f46a6"/><rect x="4" y="6" width="8" height="6" fill="#fff"/><rect x="5.5" y="3.5" width="5" height="3" fill="none" stroke="#fff"/></svg>
        (345) 555-0143
      </p>
      <p class="contact__row">
        <svg class="contact__icon" viewBox="0 0 16 16"><rect width="16" height="16" rx="2" fill="#3f46a6"/><rect x="3.5" y="5" width="9" height="6" fill="#fff"/><path d="M3.5 5l4.5 3.5L12.5 5" fill="none" stroke="#3f46a6"/></svg>
        marcus@cbds.ky
      </p>
    </div>

    <div class="edge-band">
      <span class="edge-band__web">www.cbds.ky</span>
    </div>
  </section>
</main>
</body>
</html>
```